Business cards real estate company

We need a design for a business card. It is a company that specializes in real estate sales. There should be space for a photo of the respective employee as well as the website and telephone number on it. Design should be noble, innovative.

Contact Information for Business Card

Website, Name, Position, Telefonnummer

Requirements
Must have
• Photo, logo

```html
<!DOCTYPE html>
<html lang="en">
<head>
<meta charset="utf-8">
<title>Novaterra business cards</title>
<link href="https://fonts.googleapis.com/css2?family=Montserrat:wght@400;500;700&display=swap" rel="stylesheet">
<style>
  :root {
    --backdrop: #4a4a4a;
    --card: #1c1c1c;
    --accent: #8dc63f;
    --text-light: #f2f2f2;
    --emboss: #3a3a3a;
    --photo-top: #2a2522;
    --photo-bottom: #a9c3e6;
  }
  * { margin: 0; padding: 0; box-sizing: border-box; }
  html, body { width: 1200px; height: 801px; overflow: hidden; }
  body {
    background: var(--backdrop);
    font-family: "Montserrat", sans-serif;
    position: relative;
  }
  .card {
    position: absolute;
    top: 250px;
    width: 525px;
    height: 300px;
    background: var(--card);
    border: 2px solid var(--accent);
    border-radius: 16px;
    overflow: hidden;
  }
  .card--front { left: 50px; }
  .card--back { left: 625px; }

  .employee-photo {
    position: absolute;
    left: 0;
    bottom: 0;
    width: 250px;
    height: 200px;
    background: linear-gradient(160deg, var(--photo-top) 0%, #5a4a40 40%, var(--photo-bottom) 100%);
    border-top-right-radius: 90px;
  }
  .details {
    position: absolute;
    right: 28px;
    top: 26px;
    text-align: right;
    color: var(--text-light);
  }
  .brand-name {
    color: var(--accent);
    font-weight: 700;
    font-size: 46px;
    line-height: 1;
    letter-spacing: 0.5px;
  }
  .person-name {
    color: var(--accent);
    font-weight: 700;
    font-size: 19px;
    margin-top: 14px;
  }
  .person-role {
    font-size: 14px;
    margin-top: 2px;
  }
  .address {
    font-size: 14px;
    line-height: 1.35;
    margin-top: 14px;
  }
  .contact-list {
    list-style: none;
    font-size: 14px;
    line-height: 1.45;
    margin-top: 10px;
  }
  .contact-list li {
    display: flex;
    justify-content: flex-end;
    align-items: center;
    gap: 8px;
  }
  .contact-icon { width: 11px; height: 11px; fill: var(--accent); }

  .back-brand {
    position: absolute;
    inset: 0;
    display: flex;
    align-items: center;
    justify-content: center;
    font-weight: 700;
    font-size: 66px;
    color: var(--emboss);
    letter-spacing: 1px;
  }
</style>
</head>
<body>
  <section class="card card--front">
    <div class="employee-photo" role="img" aria-label="Portrait photo of the employee"></div>
    <div class="details">
      <div class="brand-name">Novaterra</div>
      <div class="person-name">Daniel Marsh</div>
      <div class="person-role">President</div>
      <div class="address">1820 Harbor Crest Lane<br>Seaview CA 90210</div>
      <ul class="contact-list">
        <li>555-210-4187
          <svg class="contact-icon" viewBox="0 0 12 12"><path d="M2.5 1l2 2.2-1.1 1.3a7 7 0 0 0 4.1 4.1l1.3-1.1 2.2 2-1.3 1.5C6 11 1 6 1 2.3z"/></svg>
        </li>
        <li>info@novaterra.com
          <svg class="contact-icon" viewBox="0 0 12 12"><path d="M1 2.5h10v7H1z M1 2.5l5 4 5-4" fill="none" stroke="#8dc63f" stroke-width="1.4"/></svg>
        </li>
        <li>www.novaterra.com
          <svg class="contact-icon" viewBox="0 0 12 12"><circle cx="6" cy="6" r="5.5"/></svg>
        </li>
      </ul>
    </div>
  </section>

  <section class="card card--back">
    <div class="back-brand">Novaterra</div>
  </section>
</body>
</html>
```